Creative Web Design for an ERP (technology) Consulting Business

I need two pages designed for the ERP Project Management Consulting Company I am starting. One page is the home page, the other page is an important inside page.

I've looked at many different templates for sites like this, and they all look the same to me. I am working with Drafthollow designers because I want something unique.

This site will be implemented with Wordpress using the Elementor framework,

About Me ---
I have worked with Drafthollow several times before, and I have tired to do everything I can to ve helpful. In the uploads, you will find PDF's with wireframes outlning the layout of the pages, as well as explanatios for each section. There are Word documents that you can copy into text. The list below explains the files included.

Although the wireframes suggest a layout, please feel free to use your creativity - often, I find that the designs I like the most are designs I have never thought of.

About the Company --
ERP (Enterprise Resource Planning) systems are business computer systems that tie different businesss functions together. These systems are expensive and complicated, and efforts to implement them often fail. The purpose of the company is to increase the chance of success by focusing on the things that need to be right.

I have uploaded several files to help clarify what I am looking for:
• 1a - Home Page Wireframe - PDF
Wireframe for the home page with an explanation of each section.
• 1b - Home Page Text – Word
A Word document so that you can copy the text.
• 2 - Silver Kestrel Logo – ZIP
Four different versions of the company logo in Adobe Illustrator, PNG, and JPG formats. Any of the four are acceptable:
1. Logo_1 – Black on Transparent – Same Line ERP
2. Logo_2 – White on Transparent – Same Line ERP
3. Logo_3 – Black on Transparent – Big ERP on Different Line
4. Logo_4 – White on Transparent – Big ERP on Different Line
• 3a - Silver Kestrel Page Wireframe – PDF
Wireframe for he Silver Kestrel page, with explanations and a detailed breakdown of the top section.
• 3b - Silver Kestrel Text – Word
• 4 - Colors and Palettes – PDF
• 5 - Change Management Icon – EPS
• 6 – Site Map
If you wish to see it, the site map provides an idea of the entire site. The two pages circled in red are the ones I need to be designed.

Thank you for your interest in this project!

Target Market(s)

Corporate decision makers, primarily CIOs and CFOs, as well as ERP project managers and influencers.

Industry/Entity Type

Consulting

Number of Pages Required

2 page

Font styles to use
Sans Serif

Requirements
Must have
• Pages that contain the elements explained on the wireframes provided.
Nice to have
• A design that looks and feels unique
Should not have
• A typical, template layour

```html
<!DOCTYPE html>
<html lang="en">
<head>
<meta charset="utf-8">
<title>Silver Kestrel ERP Consulting</title>
<link href="https://fonts.googleapis.com/css2?family=Inter:wght@400;500;600&display=swap" rel="stylesheet">
<style>
:root{
  --ink:#1d1f24;
  --muted:#5d6068;
  --paper:#ffffff;
  --mist:#eceef1;
  --stone:#e7e9ec;
  --clay:#c98b75;
  --clay-deep:#b97862;
  --night:#1e2029;
  --night-line:#3a3d48;
  --night-text:#c9cbd2;
}
*{margin:0;padding:0;box-sizing:border-box}
html,body{width:673px;height:1200px;overflow:hidden;background:var(--paper)}
body{font-family:"Inter",Arial,sans-serif;color:var(--ink);position:relative}
h1,h2,h3,h4{font-weight:400}
.abs{position:absolute}

/* header */
.site-header{left:0;top:0;width:673px;height:48px;z-index:3}
.brand{left:23px;top:16px;display:flex;align-items:center;gap:6px;font-size:11px;font-weight:600}
.brand-mark{width:10px;height:10px;background:var(--ink)}
.main-nav{left:218px;top:19px;display:flex;gap:24px;font-size:8px;color:var(--ink)}
.main-nav .is-active{border-bottom:1px solid var(--ink);padding-bottom:2px}
.lang{left:540px;top:19px;font-size:8px}
.btn-cta{left:572px;top:10px;width:79px;height:28px;border-radius:14px;background:var(--clay);color:var(--ink);font-size:7.5px;display:flex;align-items:center;justify-content:center}

/* hero */
.hero-photo{left:0;top:0;width:673px;height:518px;
  background:linear-gradient(180deg,#eef0f2 0%,#e9ebee 38%,#c9ccd1 60%,#8e9197 78%,#55575c 100%)}
.hero-label{left:0;top:106px;width:673px;text-align:center;font-size:11px;letter-spacing:1px;color:var(--muted)}
.hero-title{left:77px;top:123px;width:480px;text-align:center;font-size:26px;line-height:34px;letter-spacing:-.3px;white-space:nowrap}
.hero-badge{left:538px;top:122px;width:36px;height:36px;border-radius:50%;background:var(--clay)}
.btn-hero{left:272px;top:241px;width:130px;height:34px;border-radius:17px;background:var(--clay);font-size:7.5px;letter-spacing:.6px;display:flex;align-items:center;justify-content:center;gap:8px}

/* grid */
.tile{overflow:hidden}
.tile-about{left:0;top:518px;width:225px;height:262px;background:var(--paper)}
.tile-method{left:225px;top:518px;width:224px;height:292px;background:var(--stone)}
.tile-goals{left:449px;top:518px;width:224px;height:262px;background:var(--clay);color:#fff}
.tile-service{left:0;top:780px;width:225px;height:225px;background:var(--night);color:#fff}
.tile-team{left:225px;top:810px;width:224px;height:195px;background:linear-gradient(160deg,#b9b2a7,#d9d6d0 45%,#8d8f95)}
.tile-partner{left:449px;top:780px;width:224px;height:225px;background:var(--paper)}

.eyebrow{font-size:9px;letter-spacing:.8px;color:var(--muted)}
.tile-title{font-size:20px;line-height:27px;letter-spacing:-.3px}
.tile-copy{font-size:7px;line-height:12.5px;color:var(--muted)}
.text-link{font-size:7px;letter-spacing:.5px;display:flex;align-items:center;gap:6px}

.tile-goals .eyebrow{color:#fff}
.goals-lead{font-size:14.5px;line-height:21px}
.goals-rule{height:1px;background:rgba(255,255,255,.5)}
.goals-sub{font-size:13px}
.goals-copy{font-size:7px;line-height:12px;color:#f3e2dc}

.tag{background:var(--clay);color:#fff;font-size:6.5px;letter-spacing:.6px;padding:2px 6px}
.service-title{font-size:13px;line-height:19px}
.tile-service .text-link{color:#fff}

.partner-lead{font-size:16.5px;line-height:23px}
.chip{height:36px;border-radius:4px;background:var(--mist);display:flex;align-items:center;gap:8px;padding:0 8px;font-size:7px}
.chip-avatar{width:20px;height:20px;border-radius:50%;background:#b7aea4}

/* footer */
.site-footer{left:0;top:1005px;width:673px;height:195px;background:var(--night);color:#fff}
.foot-head{font-size:9px;font-weight:500;letter-spacing:.3px}
.foot-copy{font-size:7px;line-height:12px;color:var(--night-text)}
.foot-list{list-style:none;font-size:7px;line-height:15px;color:var(--night-text)}
.newsletter{width:165px;height:28px;border-radius:14px;background:#fff;color:var(--ink);font-size:7px;display:flex;align-items:center;padding-left:14px}
.socials{display:flex;gap:4px}
.socials span{width:13px;height:13px;border-radius:50%}
.foot-rule{left:25px;top:1167px;width:623px;height:1px;background:var(--night-line)}
.legal{font-size:7px;color:var(--night-text)}
</style>
</head>
<body>

<div class="abs hero-photo" role="img" aria-label="Office photograph: four consultants gathered around a laptop in a bright glass building"></div>

<header class="abs site-header">
  <div class="abs brand"><span class="brand-mark"></span>Silver Kestrel</div>
  <nav class="abs main-nav">
    <span class="is-active">Home</span><span>About</span><span class="is-active">Services</span><span>Articles</span><span>Contact</span>
  </nav>
  <span class="abs lang">EN</span>
  <a class="abs btn-cta">Get Started</a>
</header>

<section class="hero">
  <p class="abs hero-label">INTRODUCTION</p>
  <h1 class="abs hero-title">Decades in pursuit of excellence in<br>ERP solutions. Let us help you<br>achieve ERP success.</h1>
  <span class="abs hero-badge"></span>
  <a class="abs btn-hero">LEARN MORE
    <svg width="16" height="6" viewBox="0 0 16 6"><path d="M0 3h15M12 0.5 15 3 12 5.5" fill="none" stroke="#1d1f24" stroke-width="0.9"/></svg>
  </a>
</section>

<article class="abs tile tile-about">
  <p class="abs eyebrow" style="left:25px;top:34px">ABOUT</p>
  <h2 class="abs tile-title" style="left:25px;top:56px;width:190px">Silver Kestrel ERP Framework</h2>
  <p class="abs tile-copy" style="left:25px;top:117px;width:180px">Every project rests on a few essentials done right. Our framework keeps scope, people, data and process aligned so the system you buy is the system you use, on time and with far less risk along the way.</p>
</article>

<article class="abs tile tile-method">
  <h2 class="abs tile-title" style="left:27px;top:56px;width:180px">The Road to Adaptive ERP Method</h2>
  <p class="abs tile-copy" style="left:27px;top:146px;width:175px">A practical method that adapts to your business, guiding each phase from planning to go live while keeping leaders informed and teams ready for change.</p>
  <a class="abs text-link" style="left:27px;top:225px">MEET CONSULTANT
    <svg width="14" height="6" viewBox="0 0 14 6"><path d="M0 3h13M10 0.5 13 3 10 5.5" fill="none" stroke="#1d1f24" stroke-width="0.9"/></svg>
  </a>
</article>

<article class="abs tile tile-goals">
  <p class="abs eyebrow" style="left:27px;top:34px">GOALS &rarr;</p>
  <p class="abs goals-lead" style="left:27px;top:60px;width:185px">Plan, lead and deliver an ERP that truly lasts.</p>
  <div class="abs goals-rule" style="left:27px;top:150px;width:170px"></div>
  <h3 class="abs goals-sub" style="left:27px;top:169px">Aligning Organisation</h3>
  <p class="abs goals-copy" style="left:27px;top:196px;width:175px">We bring leaders and teams onto one shared plan so every decision supports the goal.</p>
</article>

<article class="abs tile tile-service">
  <span class="abs tag" style="left:25px;top:42px">BUSINESS GOALS</span>
  <svg class="abs" style="left:27px;top:78px" width="12" height="12" viewBox="0 0 12 12"><path d="M1 11 10 2M4 2h6v6" fill="none" stroke="#fff" stroke-width="1.8"/></svg>
  <h3 class="abs service-title" style="left:25px;top:108px;width:175px">ERP Project and Change Management Consulting</h3>
  <a class="abs text-link" style="left:25px;top:172px">Read more
    <svg width="14" height="6" viewBox="0 0 14 6"><path d="M0 3h13M10 0.5 13 3 10 5.5" fill="none" stroke="#fff" stroke-width="0.9"/></svg>
  </a>
</article>

<div class="abs tile tile-team" role="img" aria-label="Photograph of two smiling consultants standing in an office"></div>

<article class="abs tile tile-partner">
  <svg class="abs" style="left:25px;top:54px" width="12" height="12" viewBox="0 0 12 12"><path d="M1 11 10 2M4 2h6v6" fill="none" stroke="#1d1f24" stroke-width="1.8"/></svg>
  <p class="abs partner-lead" style="left:25px;top:88px;width:180px">Partner your enterprise consulting.</p>
  <div class="abs chip" style="left:27px;top:154px;width:75px"><span class="chip-avatar"></span>Maria</div>
  <div class="abs chip" style="left:118px;top:154px;width:78px"><span class="chip-avatar"></span>Daniel</div>
</article>

<footer class="abs site-footer">
  <h4 class="abs foot-head" style="left:25px;top:34px">Silver Kestrel</h4>
  <p class="abs foot-copy" style="left:25px;top:60px;width:180px">Focused ERP guidance for leaders who need projects to succeed.</p>
  <div class="abs newsletter" style="left:25px;top:92px">Your email</div>

  <h4 class="abs foot-head" style="left:228px;top:34px">SERVICES</h4>
  <ul class="abs foot-list" style="left:228px;top:58px">
    <li>About</li><li>Consulting</li><li>Framework</li><li>Change Plans</li><li>Blog</li>
  </ul>

  <h4 class="abs foot-head" style="left:339px;top:34px">SERVICES</h4>
  <ul class="abs foot-list" style="left:339px;top:58px">
    <li>Project Recovery</li><li>ERP Selection Support</li><li>Vendor Contract Review Study</li><li>Data Migration</li><li>Training</li>
  </ul>

  <h4 class="abs foot-head" style="left:506px;top:34px">CONTACT</h4>
  <p class="abs foot-copy" style="left:506px;top:56px;width:140px;color:#fff">214 Harbour Lane, Suite 5<br>Westmoor</p>
  <p class="abs foot-copy" style="left:506px;top:88px;color:#fff">Socials</p>
  <div class="abs socials" style="left:517px;top:106px">
    <span style="background:#3f8fd2"></span><span style="background:#d9443b"></span><span style="background:#3f8fd2"></span><span style="background:#2f7fc0"></span><span style="background:#6e717a"></span>
  </div>
</footer>

<div class="abs foot-rule"></div>
<p class="abs legal" style="left:25px;top:1181px">&copy; 2024 Silver Kestrel. All rights reserved.</p>
<p class="abs legal" style="left:530px;top:1181px">EN &nbsp;English &nbsp;&nbsp; Support</p>

</body>
</html>
```